Book Title: The Harbor's Lantern. Author Name: Marisol Thackeray

We are needing a cover, spine and back cover design for a poetry book that we are publishing called The Harbor's Lantern. We are looking for an elegant, and simplistic design with a very natural, dynamic and powerful impact.

Design Idea #1 - Shiva Conch Shell with a pink or black background. See Glen Parvey Image attached for design inspiration. Simple and dynamic .
Title and Author name created in same style as the attached Glen Parvey's Lanterns and Driftwood image.

Design Idea #2 - Image of cauldron on (see cauldrons attached for ideas) black background.
See Glen Parvey Image attached for design inspiration. Simple and dynamic Title and Author name created in same style as the attached Glen Parvey's Lanterns and Driftwood image

Design Idea #3 - Image of Tree of Life (see attached images for idea of what we are looking for) Would like to see on plain white, green, black and green background.

Target Market(s)

Spiritual Women, healers, visionaries,Goddess'

Requirements
Must have
• Please see project descriptions for specific design concepts we are looking for. Please include the authors name: Marisol Thackeray on front, spine and back cover of the book

```html
<!DOCTYPE html>
<html lang="en">
<head>
<meta charset="utf-8">
<title>The Harbor's Lantern — Marisol Thackeray</title>
<link rel="stylesheet" href="https://fonts.googleapis.com/css2?family=EB+Garamond:wght@400;500&display=swap">
<style>
  :root {
    --backdrop: #555555;
    --cover-pink-light: #ec0b94;
    --cover-pink-mid: #dc0888;
    --cover-pink-deep: #c9077b;
    --hinge-line: rgba(120, 0, 60, 0.28);
    --type-ivory: #f6eef2;
    --shell-light: #e8ebe6;
    --shell-mid: #c3cac1;
    --shell-shade: #8d978c;
  }

  * { margin: 0; padding: 0; box-sizing: border-box; }

  html, body {
    width: 1200px;
    height: 1200px;
    overflow: hidden;
    background: var(--backdrop);
  }

  .canvas {
    position: relative;
    width: 1200px;
    height: 1200px;
    background: var(--backdrop);
  }

  .front-cover {
    position: absolute;
    left: 309px;
    top: 157px;
    width: 577px;
    height: 877px;
    background: linear-gradient(135deg, var(--cover-pink-light) 0%, var(--cover-pink-mid) 45%, var(--cover-pink-deep) 100%);
    color: var(--type-ivory);
    font-family: "EB Garamond", "Garamond", serif;
    text-align: center;
  }

  .cover-hinge {
    position: absolute;
    left: 40px;
    top: 0;
    width: 2px;
    height: 100%;
    background: var(--hinge-line);
  }

  .book-title {
    position: absolute;
    top: 57px;
    left: 0;
    width: 100%;
    font-weight: 500;
    font-size: 40px;
    line-height: 57px;
    letter-spacing: 0.42em;
    text-transform: uppercase;
  }

  .book-title span {
    display: block;
    padding-left: 0.42em;
  }

  .conch-photo {
    position: absolute;
    left: 218px;
    top: 357px;
    width: 131px;
    height: 226px;
    border-radius: 14px;
    background: radial-gradient(ellipse at 60% 62%, var(--shell-light) 0%, var(--shell-mid) 60%, var(--shell-shade) 100%);
  }

  .author-name {
    position: absolute;
    top: 706px;
    left: 0;
    width: 100%;
    font-weight: 400;
    font-size: 44px;
    line-height: 58px;
    letter-spacing: 0.3em;
  }

  .author-name span {
    display: block;
    padding-left: 0.3em;
  }
</style>
</head>
<body>
  <main class="canvas">
    <section class="front-cover">
      <div class="cover-hinge"></div>

      <h1 class="book-title">
        <span>The</span>
        <span>Harbor's</span>
        <span>Lantern</span>
      </h1>

      <div class="conch-photo" role="img" aria-label="Photograph of a white Shiva conch shell, spire pointing upward"></div>

      <p class="author-name">
        <span>Marisol</span>
        <span>Thackeray</span>
      </p>
    </section>
  </main>
</body>
</html>
```